Redesigned PowerPoint template for Restaurant Services Company

We need a redesigned company template for powerpoints. looking for something modern and easy to use. If we like it, we will add additional products for the design (letterhead, social media banners, etc).

Target Market(s)

restaurant owners, and franchise owners

Font styles to use
Serif
Sans Serif

Colors
0355a3
f0474d
ffffff

Requirements
Must have
• - something that uses our colors in a modern way
- easy to use
- something that is eye catching
Nice to have
• - multiple slide types (picture and text, graphic and text, bulleted text, etc)
- easy way to swap out our prospects logo and have our prospects logo displayed throughout the deck
Should not have
• should not have locked or anchored fields making it difficult to edit

```html
<!DOCTYPE html>
<html lang="en">
<head>
<meta charset="utf-8">
<title>HSG At-A-Glance</title>
<link rel="stylesheet" href="https://fonts.googleapis.com/css2?family=Lato:wght@400;700;900&display=swap">
<style>
  :root {
    --brand-blue: #0355a3;
    --brand-red: #f0474d;
    --accent-grey: #98a1aa;
    --text-dark: #3d3d3d;
    --white: #ffffff;
    --map-light: #e9eef2;
    --map-mid: #c9d6e2;
  }
  html, body {
    margin: 0;
    padding: 0;
    overflow: hidden;
    background: var(--white);
  }
  .slide {
    position: relative;
    width: 1200px;
    height: 675px;
    overflow: hidden;
    background: var(--white);
    font-family: "Lato", sans-serif;
  }
  .top-band {
    position: absolute;
    left: 0; top: 0;
    width: 1200px; height: 8px;
    background: var(--brand-blue);
  }
  .accent-bar {
    position: absolute;
    top: 45px;
    height: 8px;
    width: 365px;
  }
  .accent-bar.blue { left: 44px; background: var(--brand-blue); }
  .accent-bar.red { left: 417px; background: var(--brand-red); }
  .accent-bar.grey { left: 791px; background: var(--accent-grey); }
  .title-box {
    position: absolute;
    left: 43px; top: 60px;
    width: 1113px; height: 124px;
    background: var(--brand-blue);
    border-bottom: 5px solid var(--brand-red);
    box-sizing: border-box;
    display: flex;
    align-items: center;
    justify-content: center;
  }
  .title {
    margin: 0;
    color: var(--white);
    font-weight: 900;
    font-size: 50px;
    letter-spacing: 1px;
  }
  .facts {
    position: absolute;
    left: 74px; top: 234px;
    width: 540px;
    margin: 0;
    padding: 0;
    list-style: none;
  }
  .facts li {
    position: relative;
    padding-left: 27px;
    margin-bottom: 12px;
    color: var(--text-dark);
    font-weight: 700;
    font-size: 19.5px;
    line-height: 23.5px;
    word-spacing: 1px;
    text-align: justify;
  }
  .facts li::before {
    content: "";
    position: absolute;
    left: 2px; top: 9px;
    width: 6px; height: 6px;
    border-radius: 50%;
    background: var(--brand-red);
  }
  .keep-together { white-space: nowrap; }
  .location-map {
    position: absolute;
    left: 694px; top: 229px;
    width: 444px; height: 367px;
    background: linear-gradient(135deg, var(--map-light), var(--map-mid));
    border-left: 5px solid var(--brand-red);
    box-sizing: border-box;
    box-shadow: 4px 5px 8px rgba(0,0,0,0.35);
  }
  .footer-band {
    position: absolute;
    left: 0; top: 641px;
    width: 1200px; height: 34px;
    background: var(--brand-blue);
    color: var(--white);
    font-size: 10px;
    letter-spacing: 0.3px;
  }
  .footer-band span {
    position: absolute;
    top: 11px;
  }
  .footer-date { left: 105px; }
  .footer-url { left: 0; width: 1200px; text-align: center; }
  .footer-page { right: 42px; }
</style>
</head>
<body>
  <div class="slide">
    <div class="top-band"></div>
    <div class="accent-bar blue"></div>
    <div class="accent-bar red"></div>
    <div class="accent-bar grey"></div>

    <header class="title-box">
      <h1 class="title">HSG AT-A-GLANCE</h1>
    </header>

    <ul class="facts">
      <li>Founded and Based in Austin, TX in 2017</li>
      <li>Veteran Owned and Operated</li>
      <li>Technology, Construction, and Managed Operations Services Company Focused On the Restaurant Industry</li>
      <li>Experienced Teams of Restaurant Operators</li>
      <li>Nearshore Technology Solution Center Offering 24/7 Support</li>
      <li>Successfully Delivered Over 200 Projects Nationally <span class="keep-together">(TX, OH, MI, OK, KS)</span> Since 2017</li>
      <li>Portion Of All Profits To Benefit Veteran Charities</li>
    </ul>

    <div class="location-map" role="img" aria-label="Road map of the Austin, Texas area with a red push pin marking the city"></div>

    <footer class="footer-band">
      <span class="footer-date">4/7/2021</span>
      <span class="footer-url">WWW.HARBORLINESERVICES.COM</span>
      <span class="footer-page">2</span>
    </footer>
  </div>
</body>
</html>
```